Talvor Visit cards serious but not sad

Hello, I'd like to design my visit cards with the logo Talvor (attached) the following information: Name: Karim Belmadi Title: Mobile Director: 33 (0) 6 72 18 35 09 Phone: 33 (0) 4 58 61 07 92 e-mail: karim.belmadi@talvor-consulting.example address: 17 Rue Marcel Danvin 92400 Courbevoie This visit will be used on the banking institutions and Talvor is a consulting firm. I do not want to have dark background.

Target Market(s)

banks

Contact Information for Business Card

Name : Karim Belmadi
Title : Director
mobile : +33(0)6 72 18 35 09
Phone : +33(0)4 58 61 07 92
e-mail: karim.belmadi@talvor-consulting.example
adresse : 17 Rue marcel Danvin 92400 Courbevoie

Requirements
Nice to have
• serious but not sad

```html
<!DOCTYPE html>
<html lang="en">
<head>
<meta charset="utf-8">
<title>Talvor – Business Cards</title>
<link href="https://fonts.googleapis.com/css2?family=Exo+2:wght@400;500;700&display=swap" rel="stylesheet">
<style>
  :root {
    --stage: #3b3b3b;
    --card: #ffffff;
    --card-shade: #ececec;
    --ink-strong: #5c5c5c;
    --ink: #6f6f6f;
    --brand-grey: #8a8a8a;
    --band: #9a9a9a;
    --band-ink: #ffffff;
    --icon-bg: #9d9d9d;
  }
  * { margin: 0; padding: 0; box-sizing: border-box; }
  html, body { width: 1200px; height: 900px; overflow: hidden; }
  body {
    background: var(--stage);
    font-family: "Exo 2", "Segoe UI", sans-serif;
    position: relative;
  }
  .card {
    position: absolute;
    left: 290px;
    width: 620px;
    height: 370px;
    border-radius: 26px;
    background: linear-gradient(135deg, var(--card) 0%, var(--card) 55%, var(--card-shade) 100%);
    overflow: hidden;
    box-shadow: 0 10px 24px rgba(0,0,0,.35);
  }
  .card--front { top: 45px; }
  .card--back { top: 475px; }

  .circuit-texture {
    position: absolute;
    left: 40px;
    top: 30px;
    width: 300px;
    height: 200px;
    background: radial-gradient(ellipse at 30% 30%, rgba(0,0,0,.04), rgba(0,0,0,0) 70%);
  }

  .brand {
    position: absolute;
    display: flex;
    align-items: center;
    gap: 8px;
    color: var(--brand-grey);
    font-weight: 500;
    letter-spacing: 1px;
    line-height: 1;
  }
  .brand__dot {
    border-radius: 50%;
    background: var(--brand-grey);
    flex: none;
  }
  .card--front .brand { left: 50%; top: 47%; transform: translate(-50%, -50%); font-size: 52px; }
  .card--front .brand__dot { width: 56px; height: 56px; }
  .card--back .brand { right: 36px; top: 36px; font-size: 46px; }
  .card--back .brand__dot { width: 50px; height: 50px; }

  .contact {
    position: absolute;
    left: 44px;
    top: 142px;
    color: var(--ink);
  }
  .contact__name { font-size: 20px; font-weight: 700; color: var(--ink-strong); line-height: 26px; }
  .contact__title { font-size: 18px; line-height: 24px; margin-bottom: 12px; }
  .contact__line {
    display: flex;
    align-items: center;
    gap: 10px;
    font-size: 19px;
    line-height: 28px;
  }
  .icon {
    width: 18px; height: 18px;
    border-radius: 50%;
    background: var(--icon-bg);
    display: flex; align-items: center; justify-content: center;
    flex: none;
  }
  .icon--pin { width: 22px; height: 22px; background: var(--band-ink); }
  .address-band {
    position: absolute;
    left: 0; right: 0; bottom: 0;
    height: 60px;
    background: var(--band);
    color: var(--band-ink);
    display: flex;
    align-items: center;
    gap: 10px;
    padding-left: 44px;
    font-size: 21px;
  }
</style>
</head>
<body>
  <section class="card card--front">
    <div class="circuit-texture" role="img" aria-label="Faint circuit-trace background texture"></div>
    <div class="brand"><span class="brand__dot"></span><span class="brand__name">Talvor</span></div>
  </section>

  <section class="card card--back">
    <div class="circuit-texture" role="img" aria-label="Faint circuit-trace background texture"></div>
    <div class="brand"><span class="brand__dot"></span><span class="brand__name">Talvor</span></div>

    <div class="contact">
      <p class="contact__name">Karim Belmadi</p>
      <p class="contact__title">Director</p>
      <p class="contact__line">
        <span class="icon"><svg width="10" height="10" viewBox="0 0 10 10"><rect x="2.5" y="0.5" width="5" height="9" rx="1" fill="#fff"/></svg></span>
        +33(0)6 72 18 35 09
      </p>
      <p class="contact__line">
        <span class="icon"><svg width="11" height="11" viewBox="0 0 12 12"><path d="M2 1.5 L4.5 1 L5.5 3.5 L4 4.5 Q5 7 7.5 8 L8.5 6.5 L11 7.5 L10.5 10 Q5 10.5 1.5 5 Z" fill="#fff"/></svg></span>
        +33(0)4 58 61 07 92
      </p>
      <p class="contact__line">
        <span class="icon"><svg width="11" height="9" viewBox="0 0 11 9"><rect x="0.5" y="0.5" width="10" height="8" rx="1" fill="#fff"/><path d="M0.8 1 L5.5 5 L10.2 1" stroke="#9d9d9d" stroke-width="1" fill="none"/></svg></span>
        karim.belmadi@talvor-consulting.example
      </p>
    </div>

    <div class="address-band">
      <span class="icon icon--pin">
        <svg width="12" height="14" viewBox="0 0 12 14"><path d="M6 0.5 C3 0.5 1 2.6 1 5.2 C1 8.5 6 13.5 6 13.5 C6 13.5 11 8.5 11 5.2 C11 2.6 9 0.5 6 0.5 Z" fill="#9a9a9a"/><circle cx="6" cy="5.2" r="1.8" fill="#fff"/></svg>
      </span>
      17 Rue marcel Danvin 92990 Bellecourt
    </div>
  </section>
</body>
</html>
```